Business Card Design

Looking for a professional looking business card for a carpentry/construction business that deals with renovations, extensions, homes, and anything carpentry based in Northern Australia. Would like to incorporate the attached logo with backgrounds of white, grey or maybe a close up of timber/wood grain. Thanks

Industry/Entity Type

Carpentry

Contact Information for Business Card

Dean Carlow, Owner, Po Box 2674 Katherine NT 0851, dean-carlow@fernmail.example, 0419563072, Builders Number: 293417CR

Requirements
Should not have
• Power tools/hand tools related to carpentry

```html
<!DOCTYPE html>
<html lang="en">
<head>
<meta charset="UTF-8">
<title>Carlow Carpentry – Business Card</title>
<link rel="stylesheet" href="https://fonts.googleapis.com/css2?family=Montserrat:wght@300;400;800&display=swap">
<style>
  :root {
    --page-bg: #e6e4e1;
    --timber-dark: #a9521a;
    --timber-mid: #c86f26;
    --timber-light: #dc8f3d;
    --brand-blue: #2f5fd8;
    --text-light: #fff6ea;
    --card-shadow: rgba(40, 25, 10, 0.28);
  }
  * { margin: 0; padding: 0; box-sizing: border-box; }
  html, body {
    width: 1200px;
    height: 873px;
    overflow: hidden;
    background: var(--page-bg);
    font-family: "Montserrat", sans-serif;
  }
  .canvas {
    width: 1200px;
    height: 873px;
    display: flex;
    align-items: center;
    justify-content: center;
    gap: 60px;
  }
  .card {
    position: relative;
    width: 530px;
    height: 304px;
    border-radius: 4px;
    overflow: hidden;
    box-shadow: 0 14px 30px var(--card-shadow);
  }
  .card__timber {
    position: absolute;
    inset: 0;
    background: linear-gradient(160deg, var(--timber-light) 0%, var(--timber-mid) 45%, var(--timber-dark) 100%);
  }
  .wordmark {
    position: absolute;
    display: flex;
    align-items: center;
    gap: 10px;
    font-weight: 800;
    letter-spacing: 0.5px;
    line-height: 1;
    white-space: nowrap;
  }
  .wordmark__square {
    width: 14px;
    height: 14px;
    background: currentColor;
    flex: none;
  }
  /* front */
  .card--front .wordmark--top {
    top: 30px;
    left: 34px;
    color: var(--brand-blue);
    font-size: 22px;
  }
  .contact {
    position: absolute;
    top: 78px;
    left: 34px;
    color: var(--text-light);
  }
  .contact__name {
    font-size: 24px;
    font-weight: 400;
    letter-spacing: 0.5px;
  }
  .contact__role {
    font-size: 13px;
    font-weight: 300;
    margin: 4px 0 16px;
  }
  .contact__line {
    font-size: 11.5px;
    font-weight: 300;
    line-height: 1.65;
    letter-spacing: 0.4px;
  }
  .card--front .wordmark--bottom {
    right: 32px;
    bottom: 30px;
    color: var(--text-light);
    font-size: 28px;
  }
  /* back */
  .card--back .wordmark--centre {
    top: 50%;
    left: 50%;
    transform: translate(-50%, -50%);
    color: var(--brand-blue);
    font-size: 40px;
  }
</style>
</head>
<body>
<main class="canvas">
  <section class="card card--front" aria-label="Business card front">
    <div class="card__timber" role="img" aria-label="Close-up timber wood grain background"></div>
    <div class="wordmark wordmark--top"><span class="wordmark__square"></span>Carlow Carpentry</div>
    <div class="contact">
      <p class="contact__name">Dean Carlow</p>
      <p class="contact__role">Owner</p>
      <p class="contact__line">Po Box 2674 Ferndale NT 0899</p>
      <p class="contact__line">dean-carlow@fernmail.example</p>
      <p class="contact__line">0419563072</p>
      <p class="contact__line">BN: 293417CR</p>
    </div>
    <div class="wordmark wordmark--bottom">Carlow Carpentry</div>
  </section>

  <section class="card card--back" aria-label="Business card back">
    <div class="card__timber" role="img" aria-label="Close-up timber wood grain background"></div>
    <div class="wordmark wordmark--centre"><span class="wordmark__square"></span>Carlow Carpentry</div>
  </section>
</main>
</body>
</html>
```